KBRF website design

We need a page template website design for a cms website. Please see the brief attached for the details.
The client is the Kestrel Brook Ramfold Federation which is an organisation promoting the White Suffolk Sheep Breed within Australia.
Updates

Reason: So that my top few designs can make changes and re-submit.

Target Market(s)

See attached brief

```html
<!DOCTYPE html>
<html lang="en">
<head>
<meta charset="utf-8">
<title>Kestrel Brook Ramfold Federation</title>
<link href="https://fonts.googleapis.com/css2?family=Lato:ital,wght@0,300;0,400;0,700;0,900;1,400&family=Ubuntu:wght@400;500;700&display=swap" rel="stylesheet">
<style>
:root{
  --green:#0f5c3a;
  --green-dark:#0a4a2e;
  --nav-active:#2b2b2b;
  --yellow:#f3d22f;
  --red:#c0202a;
  --orange:#e04a2a;
  --text:#2a2a2a;
  --page:#e6e6e6;
  --footer:#231f20;
  --footer-band:#484848;
  --footer-text:#c9c9c9;
  --link-yellow:#f1d32a;
}
*{box-sizing:border-box;margin:0;padding:0}
html,body{width:1120px;height:1200px;overflow:hidden}
body{background:var(--page);font-family:'Lato',sans-serif;color:var(--text);position:relative}

.site-header{position:absolute;left:0;top:0;width:1120px;height:143px;background:#fff;box-shadow:0 3px 4px rgba(0,0,0,.25);z-index:2}
.brand{position:absolute;left:172px;top:14px;width:772px;height:72px}
.brand-mark{position:absolute;left:0;top:2px;width:66px;height:66px;border-radius:50%;background:var(--yellow);border:3px solid var(--green)}
.brand-name{position:absolute;right:0;top:4px;font-family:'Ubuntu',sans-serif;font-weight:700;font-size:35px;color:var(--green);letter-spacing:.3px;white-space:nowrap}
.brand-tagline{position:absolute;right:0;top:44px;font-size:24px;color:var(--red);font-weight:400;font-style:italic}

.main-nav{position:absolute;left:170px;top:101px;width:780px;height:42px;display:flex;background:var(--green)}
.main-nav a{display:flex;align-items:center;justify-content:center;height:100%;color:#fff;text-decoration:none;font-weight:700;font-size:13px;text-transform:uppercase;border-right:1px solid var(--green-dark)}
.main-nav a:last-child{border-right:0}
.main-nav a.active{background:var(--nav-active)}

.hero{position:absolute;left:170px;top:143px;width:780px;height:175px;background:linear-gradient(180deg,#6f7654 0%,#8b7f5c 35%,#c9a677 60%,#b98d5c 85%,#a5432a 100%)}

.panel{position:absolute;left:170px;top:318px;width:780px;height:742px;background:#fff;border-left:1px solid #d6d6d6;border-right:1px solid #d6d6d6}

.quick-links{position:absolute;left:27px;top:28px;width:224px}
.quick-card{position:relative;height:104px;margin-bottom:9px;border:1px solid #cfcfcf;border-radius:3px;background:linear-gradient(180deg,#fbfbfb,#ededed);box-shadow:0 2px 2px rgba(0,0,0,.12);display:flex;align-items:center}
.quick-icon{position:absolute;left:14px;top:17px;width:69px;height:69px;border-radius:50%;background:var(--yellow);border:3px solid var(--green);box-shadow:2px 3px 4px rgba(0,0,0,.3);display:flex;align-items:center;justify-content:center}
.quick-title{position:absolute;left:93px;font-family:'Ubuntu',sans-serif;font-weight:500;font-size:15px;line-height:19px;color:#111;text-transform:uppercase}
.quick-sub{display:block;font-family:'Lato',sans-serif;font-weight:700;font-size:11px;line-height:19px;color:var(--green)}

.sponsors{position:absolute;left:27px;top:490px;width:224px}
.sponsors h3{font-family:'Ubuntu',sans-serif;font-weight:500;font-size:15px;color:#111;margin-bottom:2px}
.sponsor-ad{width:224px;height:174px;background:var(--orange);position:relative}
.sponsor-name{position:absolute;left:20px;top:6px;color:#fff;font-family:'Ubuntu',sans-serif;font-weight:500;font-size:18px;line-height:20px}
.sponsor-photo{position:absolute;left:0;top:45px;width:224px;height:110px;background:linear-gradient(180deg,#7d8a5a,#6a4532 55%,#8b8a6a)}
.sponsor-url{position:absolute;left:0;bottom:0;width:224px;height:19px;color:#fff;font-weight:700;font-size:12.5px;text-align:center;line-height:19px}
.sponsors-more{display:block;margin-top:9px;font-size:11px;font-weight:700;color:var(--green);text-decoration:none}

.content{position:absolute;left:277px;top:26px;width:474px;font-size:12.6px;line-height:20.8px}
.welcome{font-weight:300;font-size:29px;line-height:32px;color:#222}
.welcome strong{display:block;font-family:'Ubuntu',sans-serif;font-weight:500;color:var(--green);font-size:30px;line-height:34px;margin-bottom:4px}
.content h2{font-family:'Ubuntu',sans-serif;font-weight:500;font-size:15px;color:var(--green);margin:22px 0 1px}
.content a{color:var(--green)}
.ticks{list-style:none}
.ticks li{position:relative;padding-left:16px;line-height:23.2px}
.ticks svg{position:absolute;left:0;top:7px}

.site-footer{position:absolute;left:0;top:1060px;width:1120px;height:140px;background:var(--footer);border-top:6px solid var(--footer-band);color:var(--footer-text);font-size:11px}
.copyright{position:absolute;left:170px;top:30px;line-height:21px}
.copyright a{color:var(--link-yellow);text-decoration:none}
.follow{position:absolute;left:494px;top:31px;display:flex;align-items:center;gap:10px}
.social-square{width:21px;height:21px;background:#3b5998;border-radius:2px}
.contact-list{position:absolute;left:698px;top:28px;line-height:21px}
.contact-list div{display:flex}
.contact-list dt{width:58px}
.contact-list .sep{width:29px}
</style>
</head>
<body>
<header class="site-header">
  <div class="brand">
    <div class="brand-mark"></div>
    <div class="brand-name">Kestrel Brook Ramfold Federation</div>
    <div class="brand-tagline">Stronger Flocks Ahead</div>
  </div>
  <nav class="main-nav">
    <a class="active" style="width:73px">Home</a>
    <a style="width:75px">About</a>
    <a style="width:83px">Search</a>
    <a style="width:147px">Member Services</a>
    <a style="width:108px">Stud Pages</a>
    <a style="width:70px">News</a>
    <a style="width:66px">Sales</a>
    <a style="width:68px">Links</a>
    <a style="width:90px">Contact</a>
  </nav>
</header>

<div class="hero" role="img" aria-label="Flock of white sheep standing in a line on red earth with hills behind"></div>

<main class="panel">
  <aside class="quick-links">
    <div class="quick-card">
      <span class="quick-icon">
        <svg width="30" height="30" viewBox="0 0 24 24"><path fill="#0f5c3a" d="M6.6 10.8a15 15 0 0 0 6.6 6.6l2.2-2.2a1 1 0 0 1 1-.25 11.4 11.4 0 0 0 3.6.57 1 1 0 0 1 1 1V20a1 1 0 0 1-1 1A17 17 0 0 1 3 4a1 1 0 0 1 1-1h3.5a1 1 0 0 1 1 1c0 1.25.2 2.45.57 3.57a1 1 0 0 1-.25 1z"/></svg>
      </span>
      <span class="quick-title">Prime Lamb<br>Helpline</span>
    </div>
    <div class="quick-card">
      <span class="quick-icon">
        <svg width="36" height="36" viewBox="0 0 36 36" fill="none" stroke="#0f5c3a" stroke-width="2.5"><rect x="4" y="7" width="28" height="25" rx="2"/><path d="M4 14h28M11 3v7M25 3v7M4 20h28M4 26h28M11 14v18M18 14v18M25 14v18"/></svg>
      </span>
      <span class="quick-title">Events</span>
    </div>
    <div class="quick-card">
      <span class="quick-icon">
        <svg width="40" height="34" viewBox="0 0 40 34"><circle cx="15" cy="10" r="8" fill="#0f5c3a"/><circle cx="28" cy="13" r="6" fill="#0f5c3a"/><path d="M2 32c0-10 6-13 13-13s13 3 13 13z" fill="#0f5c3a"/><path d="M24 32c0-6 0-10 5-12 6 0 9 4 9 12z" fill="#0f5c3a"/></svg>
      </span>
      <span class="quick-title" style="top:23px;left:95px">Members
        <span class="quick-sub">Members Resources</span>
        <span class="quick-sub">Webmanager Login</span>
      </span>
    </div>
    <div class="quick-card">
      <span class="quick-icon">
        <svg width="38" height="34" viewBox="0 0 38 34" fill="#0f5c3a"><path d="M4 12h8l18-9v28l-18-9H4z"/><path d="M9 22h6l2 10h-6z"/><rect x="32" y="13" width="4" height="8"/></svg>
      </span>
      <span class="quick-title">Latest<br>News</span>
    </div>
  </aside>

  <section class="sponsors">
    <h3>SPONSORS</h3>
    <div class="sponsor-ad">
      <div class="sponsor-name">PastureWire Stockyard</div>
      <div class="sponsor-photo" role="img" aria-label="Two brown and white cattle grazing in a paddock"></div>
      <div class="sponsor-url">www.pasturewirestock.com.au</div>
    </div>
    <a class="sponsors-more">VIEW ALL SPONSORS&gt;</a>
  </section>

  <article class="content">
    <h1 class="welcome">WELCOME TO<strong>Kestrel Brook Ramfold Federation</strong></h1>
    <p>Lorem ipsum dolor sit amet, consectetur adipiscing elit. Sed quis nisi euismod, fermentum tellus a, lobortis quam. <b>Vestibulum condimentum</b> mi vitae diam tristique, egestas dignissim diam mattis. <a href="#">Curabitur vel diam</a> in massa porttitor dictum id in lorem.</p>

    <h2>Vivamus faucibus ac leo ac dignissim.</h2>
    <p>Maecenas orci est, euismod facilisis feugiat sit amet, semper ut tortor. Donec eleifend accumsan nisl, nec laoreet leo iaculis sit amet. Vivamus varius arcu eu sagittis aliquam. Vivamus accumsan cursus hendrerit. <b>Vivamus eu magna rhoncus</b>, consectetur metus ac, varius lacus.</p>

    <h2>Donec ultricies, tortor quis sagittis sagittis</h2>
    <ul class="ticks">
      <li><svg width="12" height="10" viewBox="0 0 12 10"><path d="M1 5l3.5 3.5L11 1.5" fill="none" stroke="#0f5c3a" stroke-width="2.4"/></svg>Mauris erat ullamcorper augue, eu placerat diam nunc a lorem.</li>
      <li><svg width="12" height="10" viewBox="0 0 12 10"><path d="M1 5l3.5 3.5L11 1.5" fill="none" stroke="#0f5c3a" stroke-width="2.4"/></svg>Nam vulputate mauris id arcu pharetra, sed posuere quam cursus.</li>
      <li><svg width="12" height="10" viewBox="0 0 12 10"><path d="M1 5l3.5 3.5L11 1.5" fill="none" stroke="#0f5c3a" stroke-width="2.4"/></svg>Nullam eget massa vel mi posuere venenatis sed quis tortor.</li>
      <li><svg width="12" height="10" viewBox="0 0 12 10"><path d="M1 5l3.5 3.5L11 1.5" fill="none" stroke="#0f5c3a" stroke-width="2.4"/></svg>In hac habitasse platea dictumst. Fusce nisi tellus, fermentum.</li>
      <li><svg width="12" height="10" viewBox="0 0 12 10"><path d="M1 5l3.5 3.5L11 1.5" fill="none" stroke="#0f5c3a" stroke-width="2.4"/></svg>In commodo egestas magna quis placerat. Quisque adipiscing consequat nisi.</li>
    </ul>

    <h2>Cras accumsan orci mauris ut aliquam ipsum faucibus sed.</h2>
    <p>Fusce quam dui, accumsan a magna in, faucibus tristique lectus. Vestibulum sapien leo, placerat quis luctus eget, auctor et justo. Vestibulum ante ipsum primis in faucibus orci luctus et ultrices posuere cubilia Curae; <b>Duis sagittis</b>, risus ut viverra dignissim, lectus nunc iaculis arcu, et gravida est tortor ut erat. Morbi a feugiat dolor, in tristique elit. Mauris feugiat aliquam vulputate.</p>

    <h2>Vivamus faucibus ac leo ac dignissim.</h2>
    <p>Vivamus varius arcu eu sagittis aliquam. Vivamus accumsan cursus hendrerit. Vivamus eu magna rhoncus, consectetur metus ac, varius lacus.</p>
  </article>
</main>

<footer class="site-footer">
  <div class="copyright">
    Copyright Kestrel Brook Ramfold Federation<br>
    <a>Website design and development by Fernleaf Web</a>
  </div>
  <div class="follow">Follow us on: <span class="social-square"></span></div>
  <dl class="contact-list">
    <div><dt>Address</dt><span class="sep">:</span><dd>PO Box 412, Marrowby, SA 5071</dd></div>
    <div><dt>Phone</dt><span class="sep">:</span><dd>08 8000 1234</dd></div>
    <div><dt>Fax</dt><span class="sep">:</span><dd>08 8000 5678</dd></div>
    <div><dt>Email</dt><span class="sep">:</span><dd>office@ramfold.example</dd></div>
  </dl>
</footer>
</body>
</html>
```